We need a new design for our construction website

We need a new website for our wordpress site kerrowmade.co.nz

It needs to be only a few pages but sleek in design and responsive, beautifully showcasing our images and video. Currently we have
1. home
2. about us
3. contact
We need either a front page that is designed much better to showcase more content, or potentially a projects page which has images from our builds. We don't have a lot of content so the content we do have needs to be maximised by image, rather than project.

Target Market(s)

High end residential construction and renovation projects, people wanting to build a nice home, clients based in Mount Maunganui, Tauranga.

Coding

Font styles to use
Sans Serif

Colors

Designer to choose only greyscale colors for use in the design.

Requirements
Must have
• A sleek design, architectural

```html
<!DOCTYPE html>
<html lang="en">
<head>
<meta charset="utf-8">
<title>Kerrowmade — Architect with a different approach</title>
<link href="https://fonts.googleapis.com/css2?family=Montserrat:wght@400;500;700;800&family=Roboto:wght@300;400&display=swap" rel="stylesheet">
<style>
:root{
  --ink:#3a3a3c;
  --text:#555558;
  --muted:#8a8a8e;
  --rule:#9a9a9e;
  --band:#6b6b6e;
  --footer:#68686b;
  --paper:#ffffff;
  --sky-1:#c9d8e6;
  --sky-2:#e6edf3;
}
*{margin:0;padding:0;box-sizing:border-box}
html,body{width:1200px;height:3712px;overflow:hidden;background:var(--paper)}
body{position:relative;font-family:'Roboto',Arial,sans-serif;color:var(--text)}
.abs{position:absolute}
.caps{font-family:'Montserrat',Arial,sans-serif;text-transform:uppercase;letter-spacing:.22em}
.photo{position:absolute}

/* header */
.brand{left:134px;top:26px;display:flex;align-items:center;gap:14px}
.brand-mark{width:40px;height:40px;border:2px solid var(--ink);border-radius:50%}
.brand-name{font-family:'Montserrat',Arial,sans-serif;font-size:22px;letter-spacing:.38em;color:var(--ink);font-weight:400}
.nav a{position:absolute;top:40px;font-family:'Montserrat',Arial,sans-serif;font-size:11px;letter-spacing:.08em;color:var(--ink);text-decoration:none;text-transform:uppercase}

/* hero */
.hero{left:59px;top:95px;width:1141px;height:497px;background:linear-gradient(180deg,#a9c2dc 0%,#cdd9e4 45%,#aeb3b6 80%,#5f6b5a 100%)}
.hero-title{left:261px;top:290px}
.hero-title span{display:inline-block;background:#5c5c5f;color:#fff;font-family:'Montserrat',Arial,sans-serif;font-weight:800;font-size:31px;letter-spacing:.2em;line-height:36px;padding:2px 8px 2px 10px;margin-bottom:6px;text-transform:uppercase}
.hero-btn{left:265px;top:403px;width:170px;height:38px;border:2px solid #fff;color:#fff;font-size:12px;font-weight:700;display:flex;align-items:center;justify-content:center}
.slides{top:621px;font-size:12px;color:var(--muted);font-family:'Montserrat',Arial,sans-serif}
.slides .on{color:var(--ink)}

/* projects */
.tag{background:var(--band);color:#fff;font-size:11px;height:28px;display:flex;align-items:center;justify-content:center}
.label{font-size:11px;color:var(--ink);display:flex;align-items:center;gap:8px}
.label::after{content:"";display:block;height:1px;background:var(--rule);width:var(--w,80px)}
.title{font-family:'Montserrat',Arial,sans-serif;font-weight:400;font-size:26px;letter-spacing:.2em;line-height:38px;color:var(--ink);text-transform:uppercase}
.body{font-size:13px;line-height:24px;font-weight:300;color:var(--text)}

.service h3{font-family:'Montserrat',Arial,sans-serif;font-size:12px;font-weight:500;letter-spacing:.22em;color:var(--ink);text-transform:uppercase}
.service i{display:block;width:55px;height:1px;background:var(--rule);margin:14px 0 12px}
.service p{font-size:13px;line-height:22px;font-weight:300;width:250px}

.btn-outline{border:1.5px solid var(--ink);color:var(--ink);font-size:10px;display:flex;align-items:center;justify-content:center}

/* gallery feed */
.tile{position:absolute;width:294px;height:321px}

/* footer */
.footer{left:0;top:3308px;width:1138px;height:404px;background:var(--footer);color:#fff}
.footer .caps{color:#fff}
</style>
</head>
<body>

<header>
  <div class="abs brand"><span class="brand-mark"></span><span class="brand-name">KERROWMADE</span></div>
  <nav class="nav">
    <a style="left:759px">Home</a>
    <a style="left:838px">About us</a>
    <a style="left:938px">Video</a>
    <a style="left:1008px">Contact</a>
  </nav>
</header>

<section class="hero-section">
  <div class="photo hero" role="img" aria-label="Modern glass pavilion and curved white residential tower under blue sky"></div>
  <h1 class="abs hero-title"><span>Architect with a</span><br><span>different approach</span></h1>
  <a class="abs hero-btn caps">Watch video</a>
  <div class="abs slides" style="left:134px">01</div>
  <div class="abs slides" style="left:169px">02</div>
  <div class="abs" style="left:195px;top:627px;width:30px;height:1px;background:var(--ink)"></div>
  <div class="abs slides on" style="left:236px">03</div>
  <svg class="abs" style="left:1010px;top:619px" width="12" height="16" viewBox="0 0 12 16"><path d="M9 2 3 8l6 6" fill="none" stroke="#aaa" stroke-width="1.5"/></svg>
  <svg class="abs" style="left:1053px;top:619px" width="12" height="16" viewBox="0 0 12 16"><path d="M3 2l6 6-6 6" fill="none" stroke="#333" stroke-width="1.8"/></svg>
</section>

<section class="projects">
  <div class="abs" style="left:0;top:773px;width:134px;height:1px;background:var(--rule)"></div>
  <div class="abs tag caps" style="left:134px;top:746px;width:183px">Current projects</div>
  <div class="abs label caps" style="left:134px;top:840px;--w:80px">Build record</div>
  <h2 class="abs title" style="left:134px;top:870px">Linden Art Museum<br>by Kerrowmade</h2>
  <p class="abs body" style="left:134px;top:960px;width:320px">Mei an iracundia conceptam, cu agam cetero has, saperet partiendo posidonium mea ne. Sed idque persequeris accommodare cu. Eu imperdiet assueverit appellantur sea.</p>
  <div class="abs" style="left:134px;top:1099px;font-size:14px;letter-spacing:.12em;color:var(--ink)">1 / 4</div>
  <div class="photo" style="left:533px;top:748px;width:478px;height:365px;background:linear-gradient(180deg,#c8ccd1 0%,#9a9da2 45%,#6b6660 75%,#9b8a6a 90%,#8f9093 100%)" role="img" aria-label="Art museum with ribbed metal upper volume and lit glass entrance"></div>
  <div class="photo" style="left:1012px;top:748px;width:188px;height:365px;background:linear-gradient(135deg,#6f6c69 0%,#8e8a85 50%,#4c4946 100%)" role="img" aria-label="Concrete cantilevered house detail"></div>
  <svg class="abs" style="left:1065px;top:925px" width="56" height="12" viewBox="0 0 56 12"><path d="M0 6h54M48 1l6 5-6 5" fill="none" stroke="#fff" stroke-width="1"/></svg>
</section>

<section class="services">
  <div class="abs service" style="left:134px;top:1258px"><h3>Design and build</h3><i></i><p>The Design and Build process streamlines your home construction project</p></div>
  <div class="abs service" style="left:469px;top:1258px"><h3>Renovations &amp; additions</h3><i></i><p>Improving the layout and functionality of your home doesn't mean having to build</p></div>
  <div class="abs service" style="left:810px;top:1258px"><h3>Project management</h3><i></i><p>We specialise in managing your entire build project.</p></div>
</section>

<section class="about">
  <div class="photo" style="left:134px;top:1477px;width:467px;height:378px;background:linear-gradient(160deg,var(--sky-2) 0%,var(--sky-1) 45%,#b9bcbf 100%)" role="img" aria-label="Stepped white building facade rising against pale sky"></div>
  <div class="abs label caps" style="left:678px;top:1476px;--w:80px">About company</div>
  <h2 class="abs title" style="left:678px;top:1512px">We are leader in the<br>construction</h2>
  <p class="abs body" style="left:678px;top:1610px;width:395px">Mei an iracundia conceptam, cu agam cetero has, saperet partiendo posidonium mea ne. Sed idque persequeris accommodare cu. Eu imperdiet assueverit appellantur sea. Debet viderer appetere te duo, alii legimus suavitate pro ea.</p>
  <p class="abs body" style="left:678px;top:1729px;width:395px">Te has dicat ceteros mediocrem, nec an luptatum praesent. Legere legimus fabellas in nam, exerci tempor eirmod no eum.</p>
  <a class="abs btn-outline caps" style="left:678px;top:1815px;width:143px;height:38px">Contact us</a>
</section>

<section class="testimonial">
  <div class="photo" style="left:135px;top:1979px;width:238px;height:278px;background:linear-gradient(180deg,#efefef 0%,#e2e2e2 60%,#9a9492 100%)" role="img" aria-label="Portrait of client holding a folder"></div>
  <div class="abs" style="left:282px;top:2145px;width:100px;height:112px;background:var(--paper)"></div>
  <div class="abs tag caps" style="left:373px;top:2117px;width:141px;height:27px">Testimonial</div>
  <div class="abs" style="left:514px;top:2145px;width:549px;height:1px;background:var(--rule)"></div>
  <p class="abs body" style="left:328px;top:2180px;width:540px">Mei an iracundia conceptam, cu agam cetero has, saperet partiendo posidonium mea ne. Sed idque persequeris accommodare cu. Eu imperdiet assueverit appellantur sea.</p>
  <div class="abs label caps" style="left:329px;top:2257px;--w:80px;font-size:12px">Mara Ellison</div>
  <svg class="abs" style="left:134px;top:2292px" width="12" height="16" viewBox="0 0 12 16"><path d="M9 2 3 8l6 6" fill="none" stroke="#aaa" stroke-width="1.5"/></svg>
  <svg class="abs" style="left:177px;top:2292px" width="12" height="16" viewBox="0 0 12 16"><path d="M3 2l6 6-6 6" fill="none" stroke="#333" stroke-width="1.8"/></svg>
</section>

<section class="gallery-feed">
  <div class="abs label caps" style="left:134px;top:2446px;--w:80px">Follow us on Framelane</div>
  <div class="tile" style="left:135px;top:2518px;background:linear-gradient(180deg,#8fb6da 0%,#c9d6e0 55%,#b6b8ba 100%)" role="img" aria-label="Cantilevered white panelled building"></div>
  <div class="tile" style="left:454px;top:2518px;background:linear-gradient(180deg,#6f7684 0%,#8c919b 55%,#6a6d73 100%)" role="img" aria-label="Curving white architecture and urban design"></div>
  <div class="abs" style="left:476px;top:2725px;width:28px;height:28px;border:2px solid #fff;border-radius:7px"></div>
  <div class="abs caps" style="left:477px;top:2772px;font-size:11px;font-weight:700;color:#fff">Architecture &amp; urban design</div>
  <svg class="abs" style="left:477px;top:2802px" width="56" height="12" viewBox="0 0 56 12"><path d="M0 6h54M48 1l6 5-6 5" fill="none" stroke="#fff" stroke-width="1"/></svg>
  <div class="tile" style="left:771px;top:2518px;background:linear-gradient(180deg,#c7d7e5 0%,#e8ecef 60%,#d2d4d6 100%)" role="img" aria-label="White modular apartment facade"></div>
  <div class="tile" style="left:135px;top:2862px;background:linear-gradient(180deg,#c6c5c2 0%,#7f7e7a 55%,#3f7f98 100%)" role="img" aria-label="Concrete house with pool terrace"></div>
  <div class="tile" style="left:454px;top:2862px;background:linear-gradient(180deg,#5b86c2 0%,#9bb6d9 50%,#9a8f7c 80%,#3d3d3c 100%)" role="img" aria-label="Angular roof bridge over water"></div>
  <div class="tile" style="left:771px;top:2862px;background:linear-gradient(180deg,#dfe4ea 0%,#c3c8cd 55%,#6f7681 100%)" role="img" aria-label="Faceted glass and tile building"></div>
</section>

<footer class="abs footer">
  <div class="abs brand" style="left:134px;top:88px"><span class="brand-mark" style="border-color:#fff"></span><span class="brand-name" style="color:#fff">KERROWMADE</span></div>
  <p class="abs caps" style="left:134px;top:159px;width:380px;font-size:11px;line-height:24px;font-weight:500">We'd love to hear about your building project and discuss how Kerrowmade can help you design and build your dream home smarter.</p>
  <div class="abs caps" style="left:588px;top:160px;font-size:11px;color:#e0e0e0">Email address</div>
  <svg class="abs" style="left:857px;top:160px" width="14" height="14" viewBox="0 0 14 14"><path d="M1 7 13 1 9 13 7 8Z" fill="none" stroke="#fff" stroke-width="1.3"/></svg>
  <div class="abs" style="left:588px;top:187px;width:284px;height:1px;background:#d8d8d8"></div>
  <div class="abs" style="left:1039px;top:164px;width:26px;height:26px;border:1.5px solid #fff;border-radius:50%"></div>
  <div class="abs" style="left:134px;top:308px;font-size:11px;font-weight:300">© Copyright 2020 All Right Reserved. | &nbsp;Privacy Policy</div>
</footer>

</body>
</html>
```